Escrow Accounting firm needs a website design for a startup that services clients nationally.

I offer escrow accounting services for title companies and real estate attorneys. I've enclosed a logo, color palette and flyers with content that can be used for the site.

I'm looking for a similar design concept as the website below from my former employer. Please don't copy because of copyright infringement. Including for design ideas only.
www.harborlinefiduciary.com

Below is a brief write-up...
For professionals in the title insurance industry, finding a trustworthy and budget-friendly solution for escrow accounting can be daunting. When choosing the right accounting partner, title companies and law firms need a group they can rely on, and that's where we come in.

```html
<!DOCTYPE html>
<html lang="en">
<head>
<meta charset="utf-8">
<title>Keystone Escrow Partners</title>
<link href="https://fonts.googleapis.com/css2?family=Montserrat:wght@500;600;700;800&family=Poppins:wght@400;500;600&display=swap" rel="stylesheet">
<style>
:root{
  --rust:#b4644c;
  --rust-dark:#a5563f;
  --salmon:#d4876f;
  --navy:#3a4457;
  --navy-soft:#4b5569;
  --navy-deep:#1d2434;
  --ink:#2b2f38;
  --text:#4a4f5a;
  --blush:#fdf1ee;
  --white:#ffffff;
}
*{margin:0;padding:0;box-sizing:border-box}
html,body{width:1200px;height:4717px;overflow:hidden}
body{position:relative;font-family:"Poppins",sans-serif;color:var(--text);background:var(--white)}
.abs{position:absolute}
h1,h2,h3,.heading{font-family:"Montserrat",sans-serif;color:var(--ink)}
.btn{position:absolute;display:flex;align-items:center;justify-content:center;gap:8px;background:var(--rust);color:#fff;font-family:"Montserrat",sans-serif;font-weight:700;font-size:15px;border-radius:4px 18px 4px 4px;text-decoration:none}
.btn svg{width:12px;height:12px}
.photo{position:absolute}

/* hero */
.hero{position:absolute;left:0;top:0;width:1200px;height:660px;background:linear-gradient(115deg,#efebe7 0%,#dcd6d0 45%,#b9b4af 100%);overflow:hidden}
.brand{position:absolute;display:flex;align-items:center;gap:12px}
.brand-mark{width:34px;height:34px;background:var(--rust)}
.brand-name{font-family:"Montserrat",sans-serif;font-weight:600;color:var(--rust);line-height:1.05}
.brand-name small{display:block;font-size:13px;letter-spacing:1px}
.nav{position:absolute;left:470px;top:50px;display:flex;gap:52px;font-size:15px;color:var(--ink)}
.nav .active{border-bottom:2px solid var(--rust);padding-bottom:2px}
.hero h1{position:absolute;left:86px;top:234px;font-size:44px;font-weight:700;line-height:53px;text-transform:uppercase;color:#2e3440}
.slides{position:absolute;left:86px;top:570px;display:flex;align-items:center;gap:10px;font-family:"Montserrat",sans-serif;font-weight:700;color:var(--ink)}
.slides .bar{width:140px;height:2px;background:#555}
.slides .bar i{display:block;width:40px;height:2px;background:var(--rust)}
.hero-emblem{position:absolute;left:640px;top:40px;width:480px;height:480px;transform:rotate(45deg);border-radius:40px;background:linear-gradient(135deg,var(--rust) 0 50%,var(--navy) 50% 100%);opacity:.95}

/* about */
.about-photo{left:118px;top:760px;width:440px;height:440px;transform:rotate(45deg);border-radius:30px;background:linear-gradient(135deg,#d9a18d,#6b6f7a 60%,#3a4457)}
.eyebrow{font-family:"Montserrat",sans-serif;font-weight:700;font-size:12px;letter-spacing:1px;color:var(--rust);text-transform:uppercase}
.about h2{position:absolute;left:628px;top:826px;width:520px;font-size:46px;line-height:54px;font-weight:600}
.about p{position:absolute;left:628px;top:1008px;width:470px;font-size:15px;line-height:26.5px}

/* what we do */
.what{position:absolute;left:0;top:1383px;width:1200px;height:610px;background:var(--navy)}
.what h2{position:absolute;top:56px;width:1200px;text-align:center;color:#fff;font-size:44px;font-weight:700}
.wcard{position:absolute;display:flex;align-items:center;gap:22px;color:#fff;font-size:13.5px;line-height:22px}
.wcard .ico{flex:none;width:54px;height:54px}
.w1{left:86px;top:143px;width:520px;height:154px;background:var(--navy-soft);border-radius:0 0 0 60px;padding:0 190px 0 20px}
.w2{left:86px;top:315px;width:520px;height:156px;background:var(--rust-dark);border-radius:60px 0 0 0;padding:0 190px 0 20px}
.w3{left:605px;top:174px;width:509px;height:160px;background:var(--rust-dark);border-radius:0 0 60px 0;padding:0 20px 0 140px}
.w4{left:605px;top:357px;width:509px;height:158px;background:var(--navy-soft);border-radius:0 60px 0 0;padding:0 20px 0 140px}
.what-emblem{position:absolute;left:494px;top:176px;width:236px;height:236px;transform:rotate(45deg);border:12px solid #fff;border-radius:36px;background:linear-gradient(135deg,var(--rust) 0 50%,var(--navy) 50%)}

/* who */
.who h2{position:absolute;left:86px;top:2158px;font-size:44px;font-weight:700}
.who p{position:absolute;left:86px;width:460px;font-size:15px;line-height:26.5px}
.who-photo{left:720px;top:2163px;width:330px;height:330px;transform:rotate(45deg);border-radius:40px;background:linear-gradient(135deg,#e8e6e3,#a7a29c 50%,#58606e)}

/* services */
.services{position:absolute;left:0;top:2638px;width:1200px;height:660px;background:var(--blush)}
.services h2{position:absolute;left:86px;top:84px;font-size:44px;font-weight:700}
.services .intro{position:absolute;left:463px;top:52px;width:652px;font-size:15px;line-height:26.5px}
.scard{position:absolute;top:187px;width:331px;height:363px;background:#fff;box-shadow:0 6px 18px rgba(0,0,0,.06)}
.scard .photo{left:0;top:0;width:331px;height:289px}
.scard .badge{position:absolute;left:14px;top:245px;width:64px;height:64px;transform:rotate(45deg);background:#fff;border:3px solid var(--rust);border-radius:10px}
.scard .badge i{position:absolute;left:17px;top:17px;width:24px;height:24px;border:2.5px solid var(--navy);border-radius:50%;transform:rotate(-45deg)}
.scard h3{position:absolute;left:97px;top:300px;font-size:18px;line-height:26px;font-weight:700;color:var(--ink)}

/* stats */
.stats{position:absolute;left:0;top:3298px;width:1200px;height:280px;background:var(--navy);overflow:hidden}
.stats .photo{left:788px;top:0;width:412px;height:280px;background:linear-gradient(100deg,#6c6a6e,#2f3340 60%,#1f2430)}
.stats .lead{position:absolute;left:156px;top:58px;color:#fff;font-family:"Montserrat",sans-serif;font-weight:600;font-size:19px;line-height:28px}
.stats .sub{position:absolute;left:156px;top:119px;color:var(--salmon);font-family:"Montserrat",sans-serif;font-weight:600;font-size:19px}
.stats .big{position:absolute;left:152px;top:138px;font-family:"Montserrat",sans-serif;font-weight:800;font-size:88px;color:var(--salmon)}
.stats-diamond{position:absolute;left:566px;top:38px;width:206px;height:206px;transform:rotate(45deg);border-radius:26px;background:linear-gradient(135deg,var(--salmon),var(--rust-dark))}
.values{position:absolute;left:574px;top:92px;list-style:none;color:#fff;font-family:"Montserrat",sans-serif;font-weight:600;font-size:18px;line-height:37px}
.values li{display:flex;align-items:center;gap:8px}
.values svg{width:17px;height:17px}

/* contact */
.contact-card{position:absolute;left:302px;top:3651px;width:814px;height:541px;background:var(--salmon);border-radius:0 18px 18px 18px}
.contact-emblem{position:absolute;left:130px;top:3720px;width:330px;height:330px;transform:rotate(45deg);border-radius:40px;background:linear-gradient(135deg,var(--rust) 0 50%,var(--navy) 50%)}
.contact .label-top{position:absolute;left:561px;top:3728px;color:#fff;font-size:19px;letter-spacing:1px}
.contact h2{position:absolute;left:561px;top:3752px;color:#fff;font-size:46px;font-weight:600}
.field{position:absolute;border-bottom:1.5px solid rgba(255,255,255,.75);color:#fff;font-size:14px;padding-left:12px}
.contact .btn{left:573px;top:4071px;width:140px;height:47px;background:var(--navy);border-radius:4px 18px 4px 4px}

/* footer */
.footer{position:absolute;left:0;top:4265px;width:1200px;height:452px;background:var(--navy-deep);color:#9aa0ad;font-size:14px}
.footer h4{position:absolute;top:119px;font-family:"Montserrat",sans-serif;font-weight:700;font-size:15px;color:var(--salmon);padding-bottom:10px}
.footer h4::after{content:"";position:absolute;left:0;bottom:0;width:28px;height:1.5px;background:var(--salmon)}
.footer ul{position:absolute;top:172px;list-style:none;line-height:36.5px}
.footer li::before{content:"›";color:var(--salmon);margin-right:10px}
.contact-list{position:absolute;left:86px;top:194px;line-height:36.5px}
.contact-list div{display:flex;align-items:center;gap:14px}
.contact-list svg{width:15px;height:15px}
.socials{position:absolute;left:993px;top:170px;display:flex;gap:26px}
.socials i{width:16px;height:16px;border:2px solid #8f95a2;border-radius:50%}
.copy{position:absolute;left:86px;top:408px;font-size:12px}
.copy b{font-weight:400;color:var(--salmon)}
</style>
</head>
<body>

<!-- Hero -->
<section class="hero">
  <div class="photo" role="img" aria-label="Photo of hands typing on a laptop beside a notebook and glasses" style="left:0;top:0;width:1200px;height:660px;background:linear-gradient(115deg,rgba(245,242,238,.9) 0%,rgba(220,214,208,.5) 50%,rgba(160,155,150,.4) 100%)"></div>
  <div class="hero-emblem" aria-hidden="true"></div>
  <div class="brand" style="left:86px;top:30px">
    <span class="brand-mark"></span>
    <span class="brand-name" style="font-size:30px">KEYSTONE<small>ESCROW PARTNERS</small></span>
  </div>
  <nav class="nav"><span class="active">Home</span><span>About</span><span>Services</span></nav>
  <a class="btn" style="left:982px;top:36px;width:132px;height:48px">Contact Us <svg viewBox="0 0 12 12"><path d="M1 6h9M6 2l4 4-4 4" stroke="#fff" stroke-width="1.6" fill="none"/></svg></a>
  <h1>Trust us to<br>provide you with<br>peace of mind</h1>
  <a class="btn" style="left:86px;top:418px;width:156px;height:46px">Know More <svg viewBox="0 0 12 12"><path d="M1 6h9M6 2l4 4-4 4" stroke="#fff" stroke-width="1.6" fill="none"/></svg></a>
  <div class="slides"><span style="font-size:22px">01</span><span class="bar"><i></i></span><span style="font-size:13px">04</span></div>
</section>

<!-- About -->
<section class="about">
  <div class="photo about-photo" role="img" aria-label="Portrait of the firm's founder seated, framed in a diamond shape"></div>
  <div class="eyebrow abs" style="left:628px;top:810px">About Us</div>
  <h2>Escrow Accounting Services are at the heart of what We Do</h2>
  <p>Trust us to provide you with peace of mind. With Keystone Escrow Partners, you can be confident that your escrow accounting will be secure, accurate, and in complete compliance with Underwriter Requirements and Best Practices.</p>
  <a class="btn" style="left:628px;top:1172px;width:160px;height:46px">Read More <svg viewBox="0 0 12 12"><path d="M1 6h9M6 2l4 4-4 4" stroke="#fff" stroke-width="1.6" fill="none"/></svg></a>
</section>

<!-- What we do -->
<section class="what">
  <h2>What We Do</h2>
  <div class="wcard w1"><svg class="ico" viewBox="0 0 54 54"><circle cx="27" cy="24" r="16" fill="none" stroke="#d4876f" stroke-width="3"/><path d="M19 38l-3 12 11-5 11 5-3-12" fill="none" stroke="#d4876f" stroke-width="3"/></svg><span>Daily two-way reconciliation is a Best Practice Standard. Let us create a customized package that ensures your compliance and protects your reporting from audit deficiencies.</span></div>
  <div class="wcard w2"><svg class="ico" viewBox="0 0 54 54"><rect x="5" y="9" width="44" height="30" rx="3" fill="none" stroke="#fde0d6" stroke-width="3"/><path d="M20 46h14M27 39v7" stroke="#fde0d6" stroke-width="3"/><circle cx="27" cy="24" r="7" fill="none" stroke="#fde0d6" stroke-width="2.5"/></svg><span>We perform reconciliations across all accounting software systems using secure protocols aligning with TIPA Best Practice - Pillar 3 standards.</span></div>
  <div class="wcard w3"><svg class="ico" viewBox="0 0 54 54"><rect x="9" y="6" width="36" height="44" rx="3" fill="none" stroke="#fde0d6" stroke-width="3"/><circle cx="27" cy="30" r="10" fill="none" stroke="#fde0d6" stroke-width="2.5"/><path d="M27 24v6l4 3" stroke="#fde0d6" stroke-width="2.5" fill="none"/></svg><span>Comprehensive daily and monthly reports will be delivered securely using VaultShare. These reports will include a detailed breakdown of items that may require your attention. We also manage the submission of reconciliations to underwriters.</span></div>
  <div class="wcard w4"><svg class="ico" viewBox="0 0 54 54"><circle cx="18" cy="18" r="11" fill="none" stroke="#d4876f" stroke-width="3"/><path d="M6 48h42M12 48V36M22 48V30M32 48V24M42 48V16" stroke="#d4876f" stroke-width="3"/></svg><span>Our affordable rates allow your company to significantly enhance efficiency with minimal investment and focus on what matters. Pricing is based on account activity volume, and we offer discounts for multiple accounts.</span></div>
  <div class="what-emblem" aria-hidden="true"></div>
</section>

<!-- Who we are -->
<section class="who">
  <h2>Who We Are</h2>
  <p style="top:2226px">Keystone Escrow Partners has accounting experts who understand the title industry and the importance of compliance, security, and implementing precise escrow accounting procedures along with timely monthly reporting.</p>
  <p style="top:2365px;font-weight:600;color:var(--ink)">Our team of experienced professionals is the ideal solution for your needs.</p>
  <div class="photo who-photo" role="img" aria-label="Close-up of a hand typing on a laptop keyboard, framed in a diamond shape"></div>
</section>

<!-- Services -->
<section class="services">
  <h2>Our Services</h2>
  <p class="intro">For professionals in the title insurance industry, finding a trustworthy and budget-friendly solution for escrow accounting can be daunting. When choosing the right accounting partner, title companies and law firms need a group they can rely on, and that's where we come in.</p>
  <div class="scard" style="left:86px">
    <div class="photo" role="img" aria-label="Hands signing a document next to a small house model and cash" style="background:linear-gradient(135deg,#6b5a4b,#a08672 50%,#d9d2c8)"></div>
    <div class="badge"><i></i></div>
    <h3>Escrow Reconciliation<br>Services</h3>
  </div>
  <div class="scard" style="left:434px">
    <div class="photo" role="img" aria-label="Hand stamping a certified seal on a notebook" style="background:linear-gradient(135deg,#cfc9c1,#ece8e2 50%,#8a6c58)"></div>
    <div class="badge"><i></i></div>
    <h3>TIPA Best Practice<br>Certification</h3>
  </div>
  <div class="scard" style="left:782px">
    <div class="photo" role="img" aria-label="Support agent with headset working at a desktop computer" style="background:linear-gradient(135deg,#e9e9ea,#b9bcc2 55%,#6d717a)"></div>
    <div class="badge"><i></i></div>
    <h3>Data Call Services</h3>
  </div>
</section>

<!-- Stats -->
<section class="stats">
  <div class="photo" role="img" aria-label="Team of professionals reviewing a tablet together in an office"></div>
  <div class="lead">Put our knowledge and experience to<br>work for you.</div>
  <div class="sub">We want to help you achieve.</div>
  <div class="big">100%</div>
  <div class="stats-diamond" aria-hidden="true"></div>
  <ul class="values">
    <li><svg viewBox="0 0 17 17"><circle cx="8.5" cy="8.5" r="7.3" fill="none" stroke="#fff" stroke-width="1.5"/><path d="M5 8.7l2.4 2.4L12 6.4" fill="none" stroke="#fff" stroke-width="1.5"/></svg>COMPLIANCE</li>
    <li><svg viewBox="0 0 17 17"><circle cx="8.5" cy="8.5" r="7.3" fill="none" stroke="#fff" stroke-width="1.5"/><path d="M5 8.7l2.4 2.4L12 6.4" fill="none" stroke="#fff" stroke-width="1.5"/></svg>EFFICIENCY</li>
    <li><svg viewBox="0 0 17 17"><circle cx="8.5" cy="8.5" r="7.3" fill="none" stroke="#fff" stroke-width="1.5"/><path d="M5 8.7l2.4 2.4L12 6.4" fill="none" stroke="#fff" stroke-width="1.5"/></svg>INTEGRITY</li>
  </ul>
</section>

<!-- Contact -->
<section class="contact">
  <div class="contact-card"></div>
  <div class="contact-emblem" aria-hidden="true"></div>
  <div class="label-top">CONTACT</div>
  <h2>Get In Touch</h2>
  <div class="field" style="left:573px;top:3828px;width:239px;height:34px">Name</div>
  <div class="field" style="left:834px;top:3828px;width:238px;height:34px">Company Name</div>
  <div class="field" style="left:573px;top:3894px;width:239px;height:32px">Phone</div>
  <div class="field" style="left:834px;top:3894px;width:238px;height:32px">Email</div>
  <div class="field" style="left:573px;top:3956px;width:499px;height:93px">Message</div>
  <a class="btn">Submit <svg viewBox="0 0 12 12"><path d="M1 6h9M6 2l4 4-4 4" stroke="#fff" stroke-width="1.6" fill="none"/></svg></a>
</section>

<!-- Footer -->
<footer class="footer">
  <div class="brand" style="left:86px;top:108px">
    <span class="brand-mark"></span>
    <span class="brand-name" style="font-size:32px">KEYSTONE<small style="color:#5b6272">ESCROW PARTNERS</small></span>
  </div>
  <div class="contact-list">
    <div><svg viewBox="0 0 15 15"><path d="M3 1l3 3-2 2c1 2 3 4 5 5l2-2 3 3-2 2C6 14 1 9 1 3z" fill="#d4876f"/></svg>555-014-2290</div>
    <div><svg viewBox="0 0 15 15"><rect x="1" y="3" width="13" height="9" rx="1" fill="#d4876f"/><path d="M1 4l6.5 4L14 4" stroke="#1d2434" stroke-width="1.2" fill="none"/></svg>hello@keystoneescrow.com</div>
    <div><svg viewBox="0 0 15 15"><circle cx="7.5" cy="7.5" r="6.3" fill="none" stroke="#d4876f" stroke-width="1.5"/><path d="M1.5 7.5h12M7.5 1.2c-3 3.6-3 9 0 12.6M7.5 1.2c3 3.6 3 9 0 12.6" stroke="#d4876f" stroke-width="1.2" fill="none"/></svg>www.keystoneescrowpartners.com</div>
  </div>
  <h4 style="left:485px">QUICK LINKS</h4>
  <ul style="left:485px"><li>Home</li><li>About</li><li>Services</li><li>Contact Us</li></ul>
  <h4 style="left:683px">OUR SERVICES</h4>
  <ul style="left:683px"><li>Escrow Reconciliation Services</li><li>TIPA Best Practice Certification</li><li>Data Call Services</li></ul>
  <h4 style="left:993px">GET IN TOUCH</h4>
  <div class="socials"><i></i><i></i><i></i></div>
  <div class="copy">© 2024 <b>Keystone Escrow Partners</b>. All right reserved</div>
</footer>

</body>
</html>
```